RV Park - Advertising RV Park using Billboard 12 ft wide by 6 ft tall size

We need a sign for a relatively new RV Park called Pinecrest of Dalby RV Park at 4637 Warbler Road, Dalby Ridge , WS. The sign should include our web address and phone number. pinecrestdalbyrv.example, 555-213-0947. We would like to see designs that include nice color and no tacky cartoons. Final design should communicate a nice and safe RV Park. We would also like to include quick directions - Just Ahead! Left on Brindle Rd then left on Warbler Rd. (A nice motor home or RV representation may be nice but not mandatory to be included.) Classic but eye catching design. Sign is 12 ft wide by 6 ft tall in size. Will likely be vinyl printed.

```html
<!DOCTYPE html>
<html lang="en">
<head>
<meta charset="utf-8">
<title>Pinecrest of Dalby RV Park – Billboard</title>
<link rel="stylesheet" href="https://fonts.googleapis.com/css2?family=Anton&family=Quicksand:wght@600;700&display=swap">
<style>
  :root {
    --backdrop: #262626;
    --board-black: #151515;
    --board-white: #ffffff;
    --ink: #121212;
    --brand-red: #6e1410;
    --ridge-dark: #2e2e2e;
    --ridge-light: #e6e6e6;
  }
  html, body {
    margin: 0;
    padding: 0;
    width: 1060px;
    height: 1200px;
    overflow: hidden;
    background: var(--backdrop);
  }
  .billboard {
    position: absolute;
    left: 40px;
    top: 355px;
    width: 980px;
    height: 490px;
    background: var(--board-black);
    overflow: hidden;
  }
  .headline {
    position: absolute;
    left: 0;
    top: 0;
    width: 980px;
    height: 240px;
  }
  .headline text {
    font-family: "Anton", "Impact", sans-serif;
    font-size: 168px;
  }
  .address {
    position: absolute;
    left: 0;
    top: 244px;
    width: 980px;
    margin: 0;
    text-align: center;
    font-family: "Quicksand", sans-serif;
    font-weight: 700;
    font-size: 34px;
    color: var(--board-white);
    line-height: 1;
  }
  .ridge {
    position: absolute;
    left: 49px;
    top: 300px;
    width: 890px;
    height: 88px;
    background: linear-gradient(180deg, var(--ridge-dark) 0%, var(--ridge-light) 100%);
    border-radius: 60% 60% 0 0 / 100% 100% 0 0;
  }
  .contact-band {
    position: absolute;
    left: 0;
    top: 388px;
    width: 980px;
    height: 102px;
    background: var(--board-white);
  }
  .web-address {
    position: absolute;
    left: 39px;
    top: 25px;
    width: 463px;
    height: 51px;
    border-radius: 14px;
    background: var(--brand-red);
    color: var(--board-white);
    font-family: "Quicksand", sans-serif;
    font-weight: 700;
    font-size: 30px;
    line-height: 51px;
    text-align: center;
    white-space: nowrap;
  }
  .phone {
    position: absolute;
    left: 524px;
    top: 14px;
    margin: 0;
    font-family: "Quicksand", sans-serif;
    font-weight: 700;
    font-size: 64px;
    line-height: 1;
    color: var(--ink);
    white-space: nowrap;
  }
</style>
</head>
<body>
  <main class="billboard">
    <svg class="headline" viewBox="0 0 980 240" aria-label="Just Ahead!">
      <text x="490" y="216" text-anchor="middle" textLength="862" lengthAdjust="spacing"
            fill="none" stroke="var(--board-white)" stroke-width="20" stroke-linejoin="round">JUST AHEAD!</text>
      <text x="490" y="216" text-anchor="middle" textLength="862" lengthAdjust="spacing"
            fill="none" stroke="var(--board-black)" stroke-width="17" stroke-linejoin="round">JUST AHEAD!</text>
      <text x="490" y="216" text-anchor="middle" textLength="862" lengthAdjust="spacing"
            fill="var(--board-white)">JUST AHEAD!</text>
    </svg>

    <p class="address">4637 Warbler Road, Dalby Ridge , WS</p>

    <div class="ridge" role="img" aria-label="Mountain ridge silhouette in black and white"></div>

    <footer class="contact-band">
      <div class="web-address">PinecrestDalbyRV.example</div>
      <p class="phone">555-213-0947</p>
    </footer>
  </main>
</body>
</html>
```